Oil and Gas Exploration and Production company needs a business card design

We need a business card design using our logo and colors in the logo. We want a mainstream design.

```html
<!DOCTYPE html>
<html lang="en">
<head>
<meta charset="utf-8">
<title>Kestrel Oil &amp; Gas — Business Card</title>
<link rel="stylesheet" href="https://fonts.googleapis.com/css2?family=Lato:wght@400;700;900&family=Roboto:wght@500;700&display=swap">
<style>
  :root {
    --stage: #2b2b2b;
    --card-white: #ffffff;
    --card-black: #121212;
    --ink: #1a1a1a;
    --text-grey: #3d3d3d;
    --gold: #c9962b;
    --divider: #9a9a9a;
    --pattern-dark: #1c1c1c;
    --pattern-light: #8a8a8a;
  }
  * { margin: 0; padding: 0; box-sizing: border-box; }
  html, body { width: 1200px; height: 960px; overflow: hidden; }
  body {
    background: var(--stage);
    font-family: "Lato", sans-serif;
    position: relative;
  }
  .card {
    position: absolute;
    width: 600px;
    height: 343px;
    border-radius: 3px;
    box-shadow: 0 18px 40px rgba(0,0,0,0.5);
    overflow: hidden;
  }
  /* Back side */
  .card-back {
    left: 470px;
    top: 90px;
    background: var(--card-black);
  }
  .card-back .pattern {
    position: absolute;
    inset: 0;
    background: linear-gradient(160deg, var(--pattern-light) 0%, #4a4a4a 35%, var(--pattern-dark) 70%);
    opacity: 0.55;
  }
  .card-back .brand {
    position: absolute;
    right: 40px;
    bottom: 70px;
    display: flex;
    align-items: center;
    gap: 10px;
    background: var(--card-black);
    padding: 8px 14px;
  }
  .brand-dot {
    width: 14px; height: 14px;
    border-radius: 50%;
    background: var(--gold);
  }
  .card-back .brand-name {
    color: var(--card-white);
    font-weight: 900;
    font-size: 30px;
    letter-spacing: 0.5px;
  }
  /* Front side */
  .card-front {
    left: 130px;
    top: 500px;
    background: var(--card-white);
    display: flex;
    align-items: center;
  }
  .front-brand {
    width: 330px;
    display: flex;
    align-items: center;
    justify-content: center;
    gap: 12px;
  }
  .front-brand .brand-dot { width: 20px; height: 20px; }
  .front-brand .brand-name {
    color: var(--ink);
    font-weight: 900;
    font-size: 38px;
    line-height: 1.05;
  }
  .divider {
    width: 2px;
    height: 190px;
    background: var(--divider);
  }
  .details {
    padding-left: 40px;
    color: var(--text-grey);
  }
  .person-name {
    font-family: "Roboto", sans-serif;
    font-weight: 700;
    font-size: 30px;
    color: var(--gold);
    line-height: 1.1;
  }
  .person-title {
    font-family: "Roboto", sans-serif;
    font-weight: 500;
    font-size: 21px;
    color: var(--text-grey);
    margin-bottom: 20px;
  }
  .address {
    font-size: 17px;
    line-height: 1.35;
    margin-bottom: 18px;
  }
  .contact-list { list-style: none; font-size: 18px; line-height: 1.45; }
  .contact-list li { display: flex; align-items: center; gap: 10px; }
  .contact-list svg { width: 16px; height: 16px; fill: var(--gold); flex: none; }
</style>
</head>
<body>

  <section class="card card-back">
    <div class="pattern" role="img" aria-label="Repeating pattern of oil drop shapes fading from light grey to black"></div>
    <div class="brand">
      <span class="brand-dot"></span>
      <span class="brand-name">Kestrel Oil &amp; Gas</span>
    </div>
  </section>

  <section class="card card-front">
    <div class="front-brand">
      <span class="brand-dot"></span>
      <span class="brand-name">Kestrel<br>Oil &amp; Gas</span>
    </div>
    <div class="divider"></div>
    <div class="details">
      <p class="person-name">Daniel Reyes</p>
      <p class="person-title">President</p>
      <p class="address">Level 5, 27 Harbour Lane<br>Ridgeport, VIC 3100</p>
      <ul class="contact-list">
        <li>
          <svg viewBox="0 0 24 24" aria-hidden="true"><path d="M6.6 10.8a15.1 15.1 0 0 0 6.6 6.6l2.2-2.2a1 1 0 0 1 1-.25 11.4 11.4 0 0 0 3.6.57 1 1 0 0 1 1 1V20a1 1 0 0 1-1 1A17 17 0 0 1 3 4a1 1 0 0 1 1-1h3.5a1 1 0 0 1 1 1c0 1.25.2 2.45.57 3.6a1 1 0 0 1-.25 1z"/></svg>
          555 014 2287
        </li>
        <li>
          <svg viewBox="0 0 24 24" aria-hidden="true"><path d="M2 5h20v14H2z M2 5l10 8 10-8" /></svg>
          info@northvale.com
        </li>
        <li>
          <svg viewBox="0 0 24 24" aria-hidden="true"><circle cx="12" cy="12" r="10"/><path d="M2 12h20M12 2v20" stroke="#fff" stroke-width="1.5" fill="none"/></svg>
          www.northvale.com
        </li>
      </ul>
    </div>
  </section>

</body>
</html>
```